Harborline Cover Stationary Design

We require stationary design for a new Life Insurance Business, Harborline Cover based in Melbourne Australia.
The logo for this business was successfully developed using Pixel Forum (refer attached) and all stationary will incorporate this logo design.
The layout of the stationary needs to be clear, modern and of a premium quality.
The colours to be incorporated are to be the same as those in the logo, as well as black.
Stationary required:
1) Business Card
2) Letter Head
3) With Compliments Slip
4) Envelope (both A4 and DL size)
Updates
Thanks to everyone who has submitted a design.
Hi all,
Industry/Entity Type
Business
Requirements
Must have
- For the Business Card - on front:
Company Logo: refer attached
Dorian Velk
CFP, BBUS (Acc), CA
Director
417 Marlow Parade, Kestwick, VIC 3472
T: 03 9647 2250
F: 03 9682 4037
M: 0400 917 356
email: dvelk@harborlinecover.example.au
Harborline Cover Pty Ltd trading as Harborline Cover is an Authorised Representative of QRT Wealth Advisory Pty Limited (this should be at the bottom of the business card and in very small font)
Background colour on card should be white.
For the Business Card -on back:
Company Logo. The Symbol within the logo could be bigger than the text.
www.harborlinecover.example.au
Background for the back of the card could be in either Black or white.
For the Letterhead & With Compliments Slip:
T: 03 9647 2250
F: 03 9682 4037
M: 0400 917 356
E: dvelk@harborlinecover.example.au
W: www.harborlinecover.example.au
Harborline Cover Pty Ltd trading as Harborline Cover is an Authorised Representative of QRT Wealth Advisory Pty Limited ABN 46 173 509 862 AFSL No. 518904 (this should be at the bottom/footer and be in a very small font)
Envelopes:
Other Must Haves:
Choices of Font Type and Colour should be relatively consistent across each item of stationary.
There should also be consistency in the font size for the Letterhead and With Compliments Slip.

```html
<!DOCTYPE html>
<html lang="en">
<head>
<meta charset="utf-8">
<title>Harborline Cover Stationery</title>
<link href="https://fonts.googleapis.com/css2?family=Questrial&display=swap" rel="stylesheet">
<style>
:root{
  --backdrop:#7d4f28;
  --green:#aec90c;
  --green-soft:#eef3d6;
  --header-grey:#58595b;
  --mark-grey:#6d6e70;
  --ink:#231f20;
  --paper:#ffffff;
  --black:#0b0b0b;
  --shadow:0 6px 14px rgba(0,0,0,.35);
}
*{margin:0;padding:0;box-sizing:border-box}
html,body{width:1200px;height:1200px;overflow:hidden}
body{background:var(--backdrop);font-family:"Questrial",sans-serif;color:var(--ink);position:relative}
.sheet{position:absolute;box-shadow:var(--shadow);overflow:hidden}

/* brand name block */
.brand{display:flex;align-items:center;gap:6px;color:var(--mark-grey);white-space:nowrap}
.brand-dot{border-radius:50%;background:var(--green);flex:none}
.brand-name{font-weight:400;letter-spacing:.02em}

.faint-disc{position:absolute;border-radius:50%;background:var(--green-soft);opacity:.6}

/* letterhead back */
.letterhead-back{left:91px;top:275px;width:403px;height:570px;background:var(--black)}
.letterhead-back .green-band{position:absolute;left:291px;top:0;width:112px;height:100%;background:var(--green)}
.letterhead-back .white-rule{position:absolute;left:276px;top:0;width:15px;height:100%;background:var(--paper)}
.letterhead-back .seal{position:absolute;left:208px;top:36px;width:140px;height:140px;border-radius:50%;background:var(--paper)}

/* letterhead front */
.letterhead{left:172px;top:347px;width:403px;height:570px;background:var(--paper)}
.letterhead .header-band{position:absolute;left:0;top:0;width:100%;height:59px;background:var(--header-grey)}
.letterhead .brand-seal{position:absolute;left:16px;top:14px;width:88px;height:88px;border-radius:50%;background:var(--paper)}
.letterhead .brand{position:absolute;left:26px;top:40px;flex-direction:column;align-items:flex-start;gap:4px}
.letterhead .brand-dot{width:26px;height:26px}
.letterhead .brand-name{font-size:14px;line-height:1}
.letterhead .address{position:absolute;right:120px;top:18px;text-align:right;color:var(--paper);font-size:5.5px;line-height:1.4;white-space:nowrap}
.letterhead .divider{position:absolute;left:289px;top:8px;width:1px;height:44px;background:var(--paper)}
.letterhead .contacts{position:absolute;left:295px;top:9px;color:var(--paper);font-size:5.5px;line-height:1.5;list-style:none;white-space:nowrap}
.contacts li::before{content:"";display:inline-block;width:4px;height:4px;border-radius:50%;background:currentColor;margin-right:4px;vertical-align:middle}
.letterhead .footer-note{position:absolute;left:0;right:0;bottom:12px;text-align:center;font-size:6.5px;line-height:1.35}

/* business cards */
.card-back{left:710px;top:374px;width:140px;height:97px;background:var(--black)}
.card-back .brand{position:absolute;left:0;right:0;top:34px;justify-content:center;color:var(--paper)}
.card-back .brand-dot{width:12px;height:12px}
.card-back .brand-name{font-size:8px}
.card-back .web{position:absolute;left:0;right:0;bottom:6px;text-align:center;color:var(--green);font-size:4.5px}

.card-front{left:841px;top:433px;width:172px;height:98px;background:var(--paper)}
.card-front .brand{position:absolute;left:9px;top:9px}
.card-front .brand-dot{width:10px;height:10px}
.card-front .brand-name{font-size:7px}
.card-front .person{position:absolute;left:9px;top:41px;font-size:4px;line-height:1.35;white-space:nowrap}
.card-front .person .name{font-size:6.5px;line-height:1.2}
.card-front .person .street{margin-top:6px}
.card-front .contacts{position:absolute;left:94px;top:47px;font-size:4px;line-height:1.55;list-style:none;color:var(--ink);white-space:nowrap}
.card-front .contacts li::before{background:var(--green);width:3px;height:3px}
.card-front .footer-strip{position:absolute;left:0;bottom:0;width:100%;height:8px;background:var(--green);color:var(--paper);font-size:2.6px;line-height:8px;text-align:center;white-space:nowrap}

/* envelopes */
.envelope-back{left:626px;top:602px;width:423px;height:212px;background:var(--paper)}
.envelope-back svg{position:absolute;left:0;top:0}
.envelope-back .flap-dot{position:absolute;left:200px;top:20px;width:24px;height:24px;border-radius:50%;background:var(--paper);opacity:.45}

.envelope{left:698px;top:685px;width:422px;height:211px;background:var(--paper)}
.envelope .brand{position:absolute;left:16px;top:44px}
.envelope .brand-dot{width:34px;height:34px}
.envelope .brand-name{font-size:15px}
.envelope .return-address{position:absolute;left:24px;top:113px;font-size:10.5px;line-height:1.2}
.envelope .footer-band{position:absolute;left:0;bottom:0;width:100%;height:20px;background:var(--green);color:var(--paper);font-size:10.5px;line-height:20px;text-align:right;padding-right:16px}
</style>
</head>
<body>

<section class="sheet letterhead-back" aria-label="Letterhead reverse">
  <div class="white-rule"></div>
  <div class="green-band"></div>
  <div class="seal"></div>
</section>

<section class="sheet letterhead" aria-label="Letterhead">
  <div class="faint-disc" style="left:180px;top:300px;width:260px;height:260px"></div>
  <div class="header-band"></div>
  <div class="brand-seal"></div>
  <div class="brand"><span class="brand-dot"></span><span class="brand-name">Harborline Cover</span></div>
  <p class="address">417 Marlow Parade<br>Kestwick<br>VIC 3472</p>
  <div class="divider"></div>
  <ul class="contacts">
    <li>03 9647 2250</li>
    <li>0400 917 356</li>
    <li>03 9682 4037</li>
    <li>dvelk@harborlinecover.example.au</li>
    <li>www.harborlinecover.example.au</li>
  </ul>
  <p class="footer-note">Harborline Cover Pty Ltd trading as Harborline Cover is an Authorised Representative of<br>QRT Wealth Advisory Pty Limited ABN 46 173 509 862 AFSL No. 518904</p>
</section>

<section class="sheet card-back" aria-label="Business card back">
  <div class="brand"><span class="brand-dot"></span><span class="brand-name">Harborline Cover</span></div>
  <p class="web">www.harborlinecover.example.au</p>
</section>

<section class="sheet card-front" aria-label="Business card front">
  <div class="faint-disc" style="left:110px;top:-10px;width:80px;height:80px"></div>
  <div class="brand"><span class="brand-dot"></span><span class="brand-name">Harborline Cover</span></div>
  <div class="person">
    <p class="name">Dorian Velk</p>
    <p>CFP, BBUS (Acc), CA</p>
    <p>Director</p>
    <p class="street">417 Marlow Parade, Kestwick</p>
    <p>VIC 3472</p>
  </div>
  <ul class="contacts">
    <li>03 9647 2250</li>
    <li>0400 917 356</li>
    <li>03 9682 4037</li>
    <li>dvelk@harborlinecover.example.au</li>
    <li>www.harborlinecover.example.au</li>
  </ul>
  <p class="footer-strip">Harborline Cover Pty Ltd trading as Harborline Cover is an Authorised Representative of QRT Wealth Advisory Pty Limited</p>
</section>

<section class="sheet envelope-back" aria-label="Envelope reverse">
  <svg width="423" height="212" viewBox="0 0 423 212">
    <path d="M0 0H423V40C360 40 300 48 212 67C124 48 62 40 0 40Z" fill="var(--green)"/>
  </svg>
  <div class="flap-dot"></div>
</section>

<section class="sheet envelope" aria-label="DL envelope">
  <div class="faint-disc" style="left:230px;top:20px;width:200px;height:200px"></div>
  <div class="brand"><span class="brand-dot"></span><span class="brand-name">Harborline Cover</span></div>
  <p class="return-address">417 Marlow Parade, Kestwick<br>VIC 3472</p>
  <p class="footer-band">www.harborlinecover.example.au</p>
</section>

</body>
</html>
```